Marwick Business finance web design

We are a newly established business which provides invoice finance to Small Businesses in England and Wales.
Our approach is very much a funder where the small business owner can talk to the decision maker. We will guarantee on receipt of information, a decision within 24 hours.
We are not a bank so the look of the website need to be friendly but professional.
Have two types of people we are trying to attract to the website: 1) partners who are small business owners and 2) introducers who is accountants and commercial brokers who introduce us to the small businesses.
Currently no website, although domain has been reserved.
The design should be:
Professional
“Clean” Look
Designed to convey Trust and Authority.
Appeal to the small business owner.
Must incorporate:
Logo (attached)
Front page:Top tabs to other pages 1) About us 2) Services 3) Introducers 4) Contact us
Need picture and logo on page.
1) About us page- Room for talk about the company, the people and our critera.
2) Services page- We need for what invoice finance is, and 5 boxes for different services we will provide. (link on page to contact us)
3) Introducers page- We need a part for why become an introducer? Who we can help? Why we are different? (link on page to contact us)
4) Contact us page- Office address, email, tel and if possible a map and a contact me part which will email direct to us.
Text will be provided for the design, if we can see the setup of the website we will provide a part for each of the pages to support.
Styles we think convey the correct image:
www.tovelfunding.example
www.brimsorkfs.example
www.plyfunding.example
Target Market(s)
Small business owners
Industry/Entity Type
Finance
Number of Pages Required
5+ page
Look and feel

```html
<!DOCTYPE html>
<html lang="en">
<head>
<meta charset="utf-8">
<title>Marwick Business Finance</title>
<link href="https://fonts.googleapis.com/css2?family=Raleway:wght@300;400;500;600;700&family=Lato:ital,wght@0,400;0,700;1,400&display=swap" rel="stylesheet">
<style>
:root{
  --red:#e41e26;
  --ink:#222222;
  --text:#444444;
  --muted:#666666;
  --topbar:#111111;
  --grey-bg:#efefef;
  --tab-bg:#e9e9e9;
  --btn-dark:#555555;
  --label-dark:#2c2c2c;
  --footer:#2a2a2a;
  --footer-text:#d6d6d6;
  --rule:#cfcfcf;
}
*{margin:0;padding:0;box-sizing:border-box}
html,body{width:1200px;height:3035px;overflow:hidden}
body{font-family:'Lato',sans-serif;color:var(--text);background:#fff;position:relative}
.abs{position:absolute}
section,header,footer{position:absolute;left:0;width:1200px}

/* top bar */
.topbar{top:0;height:36px;background:var(--topbar)}
.topbar .phone{left:850px;top:0;height:36px;display:flex;align-items:center;gap:8px;color:#eee;font-size:14px}
.topbar .auth{left:973px;top:0;width:126px;height:36px;background:var(--red);color:#fff;font-size:13px;font-weight:700;display:flex;align-items:center;justify-content:center;gap:12px}

/* header */
.site-header{top:36px;height:116px;background:#fff}
.brand{left:101px;top:30px;display:flex;align-items:center;gap:10px}
.brand-mark{width:18px;height:18px;border-radius:50%;background:var(--red)}
.brand-name{font-family:'Raleway',sans-serif;font-weight:700;font-size:46px;color:var(--ink);letter-spacing:-1px}
.nav a{position:absolute;top:48px;font-family:'Raleway',sans-serif;font-size:14px;font-weight:500;color:#333;text-decoration:none;letter-spacing:.3px}
.nav a.active{color:var(--red);font-weight:700}
.nav a.active::after{content:"";position:absolute;left:-4px;right:-4px;bottom:-8px;height:2px;background:var(--red)}

/* hero */
.hero{top:152px;height:601px}
.hero-photo{position:absolute;inset:0;background:linear-gradient(100deg,#dfe6ec 0%,#b9c7d3 30%,#6d7f93 55%,#3d4a5c 80%,#1f2836 100%)}
.hero-label{left:99px;top:299px;width:447px;height:111px;background:rgba(40,40,40,.8);padding:22px 0 0 32px;color:#fff;font-family:'Raleway',sans-serif;font-weight:600;font-size:30px;line-height:37px}

/* section titles */
.sec-title{left:0;width:1200px;text-align:center;font-family:'Raleway',sans-serif;font-weight:400;font-size:40px;color:var(--ink)}
.sec-title strong{color:var(--red);font-weight:700}
.divider{height:2px;width:46px;background:var(--rule)}

/* services */
.services{top:753px;height:592px;background:#fff}
.card{top:155px;width:314px;height:330px;background:#fff;box-shadow:0 2px 8px rgba(0,0,0,.18);padding:8px}
.card-img{position:relative;width:298px;height:174px;background:linear-gradient(135deg,#d9e4ee,#8ea9c4)}
.card-img.warm{background:linear-gradient(135deg,#f3e6d6,#c9b29a)}
.card-img.blue{background:linear-gradient(135deg,#6f9fd8,#1e4f93)}
.card-label{position:absolute;left:0;bottom:0;width:100%;height:42px;background:rgba(40,40,40,.88);color:#fff;font-family:'Raleway',sans-serif;font-weight:600;font-size:19px;line-height:42px;padding-left:12px}
.card-label.red{background:var(--red)}
.card p{margin:14px 6px 0;font-size:13px;line-height:20px;color:#555}
.btn{display:inline-block;background:var(--btn-dark);color:#fff;font-size:11px;font-weight:700;padding:0 12px;height:31px;line-height:31px;text-transform:uppercase;letter-spacing:.2px}
.btn.red{background:var(--red)}
.card .btn{position:absolute;left:14px;top:267px}

/* about */
.about{top:1345px;height:490px;background:var(--grey-bg)}
.video{left:99px;top:67px;width:449px;height:352px;border:6px solid #fff;box-shadow:0 6px 14px rgba(0,0,0,.22);background:linear-gradient(120deg,#c8d3dd,#8093a6 60%,#4d5b6a)}
.about h2{left:599px;top:60px;font-family:'Raleway',sans-serif;font-weight:400;font-size:33px;color:var(--ink)}
.about h2 strong{color:var(--red);font-weight:700}
.about p{left:599px;top:158px;width:505px;font-size:14px;line-height:25.7px;color:#444}

/* introducers */
.introducers{top:1835px;height:427px;background:#fff}
.intro-lead{left:140px;top:150px;width:920px;text-align:center;font-size:16px;line-height:26px;color:#333}
.tab{left:99px;width:500px;height:37px;background:var(--tab-bg);display:flex;align-items:center;padding-left:18px;gap:20px;font-family:'Raleway',sans-serif;font-weight:700;font-size:15px;color:#333}
.tab.open{background:var(--red);color:#fff;width:508px}
.tab.open::after{content:"";position:absolute;right:-14px;top:0;border-left:14px solid var(--red);border-top:18.5px solid transparent;border-bottom:18.5px solid transparent}
.intro-text{left:637px;top:239px;width:466px;font-size:14px;line-height:24px;color:#444}

/* testimonials */
.testimonials{top:2262px;height:441px;background:#f0f0f0}
.quote{left:212px;top:164px;width:830px;text-align:center;font-style:italic;font-size:13.5px;line-height:24px;color:#555}
.qmark{font-family:Georgia,serif;font-size:70px;color:#c8c8c8;line-height:1}
.quote-rule{left:247px;top:265px;width:704px;height:1px;background:#cccccc}
.avatar{top:291px;width:70px;height:70px;border-radius:50%;background:linear-gradient(160deg,#9a9a9a,#4a4a4a);border:3px solid #fff;box-shadow:0 1px 4px rgba(0,0,0,.3)}
.avatar.active{border-color:var(--red);background:linear-gradient(160deg,#e8d9c8,#b08f74)}
.t-name{left:0;width:1200px;top:370px;text-align:center;color:var(--red);font-weight:700;font-size:14px}

/* footer */
.site-footer{top:2703px;height:285px;background:var(--footer);color:var(--footer-text)}
.site-footer h4{position:absolute;top:46px;font-family:'Raleway',sans-serif;font-weight:700;font-size:16px;color:#fff}
.links{left:99px;top:86px;list-style:none}
.links li{height:35.5px;font-size:13.5px;display:flex;align-items:center;gap:14px}
.links li::before{content:"";border-left:5px solid #fff;border-top:4px solid transparent;border-bottom:4px solid transparent}
.contact-row{left:283px;display:flex;gap:18px;font-size:13.5px;line-height:20px}
.contact-row svg{flex:none;margin-top:2px}
.field{left:623px;width:215px;background:#fff;border:1px solid #bbb;font-size:12px;color:#555;padding:3px 8px}
.submit{left:623px;top:212px;width:85px;height:23px;background:var(--red);color:#fff;font-weight:700;font-size:13px;text-align:center;line-height:23px}
.vsep{top:46px;width:1px;height:200px;background:#3d3d3d}
.foot-brand{left:904px;top:128px;font-family:'Raleway',sans-serif;font-weight:700;font-size:46px;color:#fff;letter-spacing:-1px}
.copyright{top:2988px;height:47px;background:var(--red);color:#fff;text-align:center;font-size:13.5px;line-height:47px}
</style>
</head>
<body>

<header class="topbar">
  <div class="abs phone">
    <svg width="14" height="14" viewBox="0 0 24 24"><path fill="#fff" d="M6.6 10.8a15.1 15.1 0 0 0 6.6 6.6l2.2-2.2c.3-.3.7-.4 1-.2 1.1.4 2.3.6 3.6.6.6 0 1 .4 1 1V20c0 .6-.4 1-1 1A17 17 0 0 1 3 4c0-.6.4-1 1-1h3.5c.6 0 1 .4 1 1 0 1.3.2 2.5.6 3.6.1.3 0 .7-.2 1z"/></svg>
    123 456 7890
  </div>
  <div class="abs auth"><span>Login</span><span>|</span><span>Signup</span></div>
</header>

<header class="site-header">
  <div class="abs brand"><span class="brand-mark"></span><span class="brand-name">Marwick</span></div>
  <nav class="nav">
    <a class="active" style="left:486px">HOME</a>
    <a style="left:593px">ABOUT US</a>
    <a style="left:724px">SERVICES</a>
    <a style="left:854px">NTRODUCERS</a>
    <a style="left:1010px">CONTACT US</a>
  </nav>
</header>

<section class="hero">
  <div class="hero-photo" role="img" aria-label="Photo of two businessmen in suits reviewing work together in a bright office"></div>
  <div class="abs hero-label">Improve Your Business<br>Cash Flow Fast</div>
</section>

<section class="services">
  <h2 class="abs sec-title" style="top:44px">Our <strong>Services</strong></h2>
  <div class="abs divider" style="left:577px;top:118px"></div>

  <article class="abs card" style="left:101px">
    <div class="card-img" role="img" aria-label="Photo of hands pointing at financial charts on a desk"><div class="card-label">Invoice Factoring</div></div>
    <p>Amolestie consequat, v i dolore eu feugiat nulla facilisis at ve eros accumsan iusto consequat, ve eu feugiat nulfacilisi..</p>
    <span class="btn">Read more »</span>
  </article>
  <article class="abs card" style="left:445px">
    <div class="card-img warm" role="img" aria-label="Photo of hands using a calculator over paperwork"><div class="card-label red">Invoice Discounting</div></div>
    <p>Amolestie consequat, v i dolore eu feugiat nulla facilisis at ve eros accumsan iusto consequat, ve eu feugiat nulfacilisi..</p>
    <span class="btn red">Read more »</span>
  </article>
  <article class="abs card" style="left:787px">
    <div class="card-img blue" role="img" aria-label="Photo of colleagues reviewing blue financial documents"><div class="card-label">Account Receivable</div></div>
    <p>Amolestie consequat, v i dolore eu feugiat nulla facilisis at ve eros accumsan iusto consequat, ve eu feugiat nulfacilisi..</p>
    <span class="btn">Read more »</span>
  </article>
</section>

<section class="about">
  <div class="abs video" role="img" aria-label="Video still of business people shaking hands across a meeting table">
    <svg class="abs" style="left:190px;top:146px" width="48" height="48" viewBox="0 0 48 48"><circle cx="24" cy="24" r="23" fill="rgba(255,255,255,.55)"/><path d="M19 14l14 10-14 10z" fill="#fff"/></svg>
  </div>
  <h2 class="abs">Know About <strong>Marwick Finance</strong></h2>
  <div class="abs divider" style="left:599px;top:127px"></div>
  <p class="abs">Lorem Ipsum is simply dummy text of the printing and typesetting industry. Lorem Ipsum has been the industry's standard dummy text ever since the 1500s, when an unknown printer took a galley of type and scrambled it to make a type specimen book. It has survived not only five centuries, but also the leap into electronic typesetting, remaining essentially unchanged. It was popularised in the 1960s with the release of Typeline sheets containing Lorem Ipsum passages, and more recently with desktop publishing software like Quillset Layout including versions of Lorem Ipsum.</p>
  <span class="abs btn" style="left:599px;top:389px">Read more »</span>
</section>

<section class="introducers">
  <h2 class="abs sec-title" style="top:52px">Our <strong>Introducers</strong></h2>
  <div class="abs divider" style="left:577px;top:124px"></div>
  <p class="abs intro-lead">Ut enim ad minim veniam, quis nostrud exercitation ullamco laboris nisi ut aliquip ex ea commodo consequat. Duis aute irure dolor in reprehenderit in voluptate velit esse cillum dolore eu fugiat nulla pariatur. Excepteur sint occaecat cupidatat non proident</p>

  <div class="abs tab open" style="top:245px">
    <svg width="14" height="14" viewBox="0 0 14 14"><circle cx="7" cy="7" r="6" fill="none" stroke="#fff" stroke-width="1.4"/><path d="M4.2 7.2l2 2 3.6-4" fill="none" stroke="#fff" stroke-width="1.4"/></svg>
    We Need A Part For Why Become An Introducer?
  </div>
  <div class="abs tab" style="top:291px">
    <svg width="14" height="14" viewBox="0 0 14 14"><circle cx="7" cy="7" r="6" fill="none" stroke="#555" stroke-width="1.4"/><path d="M4.2 7.2l2 2 3.6-4" fill="none" stroke="#555" stroke-width="1.4"/></svg>
    Who We Can Help?
  </div>
  <div class="abs tab" style="top:340px">
    <svg width="14" height="14" viewBox="0 0 14 14"><circle cx="7" cy="7" r="6" fill="none" stroke="#555" stroke-width="1.4"/><path d="M4.2 7.2l2 2 3.6-4" fill="none" stroke="#555" stroke-width="1.4"/></svg>
    Why We Are Different?
  </div>

  <p class="abs intro-text">Lorem ipsum dolor sit amet, consectetur adipiscing elit, sed do eiusmod tempor incididunt ut labore et dolore magna aliqua. Ut enim ad minim veniam, quis nostrud exercitation ullamco laboris nisi ut aliquip ex ea commodo consequat. Duis aute irure dolor in reprehenderit in voluptate velit esse cillum dolore eu fugiat nulla pariatur.</p>
</section>

<section class="testimonials">
  <h2 class="abs sec-title" style="top:52px">What People Say <strong>About Us!</strong></h2>
  <span class="abs qmark" style="left:160px;top:148px">&ldquo;</span>
  <p class="abs quote">Lorem ipsum dolor sit amet, consectetur adipiscing elit, sed do eiusmod tempor incididunt ut labore et dolore magna aliqua. Ut enim ad minim veniam, quis nostrud exercitation ullamco laboris nisi ut aliquip ex ea commodo consequat. Duis aute irure dolor in reprehenderit in voluptate velit esse cillum dolore eu fugiat nulla pariatur. Excepteur sint occaecat cupidatat non proident, sunt in culpa qui</p>
  <span class="abs qmark" style="left:932px;top:210px">&rdquo;</span>
  <div class="abs quote-rule"></div>
  <div class="abs avatar" role="img" aria-label="Portrait photo of a client" style="left:469px"></div>
  <div class="abs avatar active" role="img" aria-label="Portrait photo of the featured client" style="left:564px"></div>
  <div class="abs avatar" role="img" aria-label="Portrait photo of a client" style="left:657px"></div>
  <div class="abs t-name">Lorem Ipsum</div>
</section>

<footer class="site-footer">
  <h4 style="left:99px">Quick Links</h4>
  <ul class="abs links">
    <li>Home</li><li>About Us</li><li>Services</li><li>Introducers</li><li>Contact Us</li>
  </ul>

  <div class="abs vsep" style="left:247px"></div>
  <h4 style="left:273px">Contact Information</h4>
  <div class="abs contact-row" style="top:90px">
    <svg width="12" height="16" viewBox="0 0 12 16"><path d="M6 0a6 6 0 0 0-6 6c0 4.5 6 10 6 10s6-5.5 6-10a6 6 0 0 0-6-6zm0 8.3A2.3 2.3 0 1 1 6 3.7a2.3 2.3 0 0 1 0 4.6z" fill="#fff"/></svg>
    <div><b style="color:#fff">Marwick Business Finance Limited</b><br>Donec porttitor entu suscipit Nsequat<br>sem cursus digni ssim</div>
  </div>
  <div class="abs contact-row" style="top:178px">
    <svg width="14" height="14" viewBox="0 0 24 24"><path fill="#fff" d="M6.6 10.8a15.1 15.1 0 0 0 6.6 6.6l2.2-2.2c.3-.3.7-.4 1-.2 1.1.4 2.3.6 3.6.6.6 0 1 .4 1 1V20c0 .6-.4 1-1 1A17 17 0 0 1 3 4c0-.6.4-1 1-1h3.5c.6 0 1 .4 1 1 0 1.3.2 2.5.6 3.6.1.3 0 .7-.2 1z"/></svg>
    <span>123 456 7890</span>
  </div>
  <div class="abs contact-row" style="top:221px">
    <svg width="14" height="12" viewBox="0 0 14 12"><rect x="0.5" y="1" width="13" height="10" fill="none" stroke="#fff"/><path d="M1 1.5l6 5 6-5" fill="none" stroke="#fff"/></svg>
    <span>info@marwickfinance.example</span>
  </div>

  <div class="abs vsep" style="left:597px"></div>
  <h4 style="left:623px">Quick Inquiry</h4>
  <div class="abs field" style="top:85px;height:24px">Name</div>
  <div class="abs field" style="top:117px;height:24px">Email</div>
  <div class="abs field" style="top:149px;height:53px">Message</div>
  <div class="abs submit">Submit</div>

  <div class="abs vsep" style="left:874px"></div>
  <div class="abs foot-brand">Marwick</div>
</footer>

<div class="abs copyright" style="left:0;width:1200px">Copyright 2016 Marwick Business Finance Limited. All rights reserved.</div>

</body>
</html>
```